Geschäftspapiere für Termin Startup
Zielgruppe
Wir sind ein Startup, das über die Seite Planorix.de (derzeit noch in der Beta-Phase)zukünftig folgenden Service anbietet: Unternehmer können sehr flexibel (selbst) gestaltete Terminformulare erstellen und auf Ihrer Website einbinden. Kunden können dann diese Termine buchen und bekommen dann Erinnerungs-Mails und SMS.
Zielgruppe: Dienstleister wie Fotografen, Friseure, Versicherungsvertreter, Masseure, Restaurants, Arztpraxen. Also alle, die darauf angewiesen sind, dass vereinbarte Termine eingehalten werden und die die Terminvereinbarung vereinfachen wollen. Also weniger per Telefon, mehr über die eigene Website.
Dateien bitte beachten für die Ansicht des Look & Feels:
https://ablage.beispielwolke.de/open?id=7QmrtHkWz2LpA94bNc3sVyTeOx8dGJuR_
Bonus-Aktion: Wir zahlen pauschal jeweils 30,00 Euro an die Designer auf den Plätzen 2 bis 4 für die geleistete Arbeit. Nur einer kann gewinnen und den Zuschlag bekommen. Aber so möchten wir gerne die Arbeit dennoch honorieren.
Aufgabenstellung
Wir benötigen ein modernes Briefpapier-Layout passend zu unserem CD.
Gerne darf/soll der ORBO (siehe Maskottchen in https://ablage.beispielwolke.de/open?id=5PwqNsYt8BaLmr2Hc7xkDuQOEPfjWzVbn )darauf erscheinen.
Maskottchen ORBO gibt es in mehreren Varianten. Siehe https://ablage.beispielwolke.de/ordner/8TrnWqLeHd5XcmZ3sJ4yPvBkGfQaNuRox?teilen=ja
Auch als Variante, das Maskottchen ORBO gegen das Logo gelehnt ist, kann genutzt werden: https://ablage.beispielwolke.de/open?id=3MuxBgTpW7RkaNj6yVqLeDsHcZoPfGtYi
Das Thema 'Terminvereinbarung' soll sofort erfasst werden mittels des Layouts bzw. der grafischen Elemente.
Auch die Branchen-Icons ( https://ablage.beispielwolke.de/ordner/6HpvRtNmQ2WkzLx8yEcBaJdFsUoGiTbeq?teilen=ja ) dürfen verwendet werden.

```html
<!DOCTYPE html>
<html lang="de">
<head>
<meta charset="utf-8">
<title>Planorix Briefpapier</title>
<link href="https://fonts.googleapis.com/css2?family=Exo+2:wght@300;400;600;700&display=swap" rel="stylesheet">
<style>
  :root {
    --green: #8cc63f;
    --text: #5c666e;
    --heading: #55606a;
    --footer-bg: #8b939b;
    --red: #e2312d;
    --yellow: #f5c400;
    --paper: #ffffff;
    --faint: #eceeef;
    --icon-ring: #7d878f;
  }
  * { margin: 0; padding: 0; box-sizing: border-box; }
  html, body { width: 848px; height: 1200px; overflow: hidden; background: var(--paper); }
  body { font-family: "Exo 2", sans-serif; color: var(--text); font-weight: 400; }
  .letter { position: relative; width: 848px; height: 1200px; overflow: hidden; }

  .header-line { position: absolute; top: 77px; left: 0; width: 848px; height: 2px; background: var(--green); }
  .branch-icon { position: absolute; top: 54px; width: 46px; height: 46px; border-radius: 50%; background: var(--paper); border: 2px solid var(--icon-ring); }
  .branch-icon::after { content: ""; position: absolute; inset: 6px; border-radius: 50%; background: linear-gradient(135deg, var(--green), #6b7880); opacity: .55; }

  .brand-block { position: absolute; top: 52px; left: 292px; width: 270px; height: 62px; background: var(--paper); }
  .brand-name { position: absolute; top: 0; left: 0; width: 100%; display: flex; align-items: center; justify-content: center; gap: 10px; height: 44px; }
  .brand-square { width: 30px; height: 30px; background: var(--green); flex: none; }
  .brand-text { font-size: 34px; font-weight: 600; color: var(--heading); line-height: 1; }
  .brand-claim { position: absolute; top: 46px; left: 0; width: 100%; text-align: center; font-size: 12px; font-weight: 400; color: var(--heading); line-height: 14px; }

  .sender-line { position: absolute; top: 172px; left: 100px; font-size: 10.5px; color: var(--heading); }
  .sender-line b { font-weight: 600; }
  .recipient { position: absolute; top: 201px; left: 100px; font-size: 13.5px; line-height: 18.5px; color: var(--heading); font-style: normal; }
  .contact { position: absolute; top: 201px; left: 505px; font-size: 13.5px; line-height: 18px; color: var(--heading); }
  .contact p { margin-bottom: 13px; }
  .contact b { font-weight: 600; }

  .subject { position: absolute; top: 393px; left: 100px; font-size: 16px; font-weight: 600; color: var(--heading); }
  .body-text { position: absolute; top: 457px; left: 100px; width: 632px; font-size: 13.3px; line-height: 19px; color: var(--heading); text-align: justify; hyphens: auto; }
  .body-text p { margin-bottom: 10px; }
  .closing { margin-top: 8px; }
  .signature { display: block; width: 60px; height: 22px; margin: 8px 0 4px; background: linear-gradient(90deg, #4a5259, #8b939b); border-radius: 3px; opacity: .7; }
  .signer { font-size: 9.5px; line-height: 13px; }

  .gear-decoration { position: absolute; left: 390px; top: 700px; width: 640px; height: 640px; border-radius: 50%; background: radial-gradient(circle, rgba(236,238,239,0) 52%, var(--faint) 53%, var(--faint) 64%, rgba(236,238,239,0) 65%); }
  .mascot { position: absolute; left: 545px; top: 838px; width: 303px; height: 241px; border-radius: 110px 40px 0 0; background: linear-gradient(160deg, #8cc63f 0%, #c9d2d7 55%, #ffffff 100%); }

  .footer-stripe { position: absolute; top: 1079px; left: 0; width: 848px; height: 4px; display: flex; }
  .footer-stripe span:nth-child(1) { flex: 0 0 38%; background: var(--green); }
  .footer-stripe span:nth-child(2) { flex: 0 0 28%; background: var(--red); }
  .footer-stripe span:nth-child(3) { flex: 1; background: var(--yellow); }
  .footer { position: absolute; top: 1083px; left: 0; width: 848px; height: 117px; background: var(--footer-bg); color: #fff; font-size: 10px; line-height: 14.4px; }
  .footer-col { position: absolute; top: 16px; }
  .footer-col b { font-weight: 700; }
  .footer-col .brand { font-weight: 700; }
</style>
</head>
<body>
<main class="letter">
  <div class="header-line"></div>
  <div class="branch-icon" role="img" aria-label="Branchen-Icon Arztpraxis" style="left:60px"></div>
  <div class="branch-icon" role="img" aria-label="Branchen-Icon Friseur" style="left:146px"></div>
  <div class="brand-block">
    <div class="brand-name"><span class="brand-square"></span><span class="brand-text">Planorix</span></div>
    <div class="brand-claim">Online-Terminbuchung</div>
  </div>
  <div class="branch-icon" role="img" aria-label="Branchen-Icon Restaurant" style="left:643px"></div>
  <div class="branch-icon" role="img" aria-label="Branchen-Icon Versicherung" style="left:732px"></div>

  <div class="sender-line"><b>Planorix GmbH</b> | Ahornweg 23 | 54321 Beispielstadt</div>

  <address class="recipient">
    Friseursalon Kammglanz<br>
    Frau Lena Wörner<br>
    Lindenhof 9<br>
    10437 Berlin
  </address>

  <div class="contact">
    <p><b>Ansprechpartner:</b> Jonas Keller</p>
    <p><b>Abteilung:</b> Kundenservice</p>
    <p><b>Telefon:</b> 04567 - 21 90 35 -12<br>
       <b>Telefax:</b> 04567 - 21 90 35 -134<br>
       <b>E-Mail:</b>&nbsp; j.keller@planorix.de</p>
    <p><b>Datum:</b>&nbsp; 24. Juni 2018</p>
  </div>

  <h1 class="subject">Betreffzeile Lorem ipsum dolor sit amet</h1>

  <div class="gear-decoration" aria-hidden="true"></div>

  <div class="body-text">
    <p>Sehr geehrte Frau Wörner,</p>
    <p>lorem ipsum dolor sit amet, consetetur sadipscing elitr, sed diam nonumy eirmod tempor invidunt ut labore et dolore magna aliquyam erat, sed diam voluptua. At vero eos et accusam et justo duo dolores et ea rebum. Stet clita kasd gubergren, no sea takimata sanctus est Lorem ipsum dolor sit amet. Lorem ipsum dolor sit amet, consetetur sadipscing elitr, sed diam nonumy eirmod tempor invidunt ut labore et dolore magna aliquyam erat, sed diam voluptua. At vero eos et accusam et justo duo dolores et ea rebum. Stet clita kasd gubergren, no sea takimata sanctus est Lorem ipsum dolor sit amet. Lorem ipsum dolor sit amet, consetetur sadipscing elitr, sed diam nonumy eirmod tempor invidunt ut labore et dolore magna aliquyam erat, sed diam voluptua. At vero eos et accusam et justo duo dolores et ea rebum. Stet clita kasd gubergren, no sea takimata sanctus est Lorem ipsum dolor sit amet.</p>
    <p>Duis autem vel eum iriure dolor in hendrerit in vulputate velit esse molestie consequat, vel illum dolore eu feugiat nulla facilisis at vero eros et accumsan et iusto odio dignissim qui blandit praesent luptatum zzril delenit augue duis dolore te feugait nulla facilisi. Lorem ipsum dolor sit amet, consectetuer adipiscing elit, sed diam nonummy nibh euismod tincidunt ut laoreet dolore magna aliquam erat volutpat.</p>
    <p>Ut wisi enim ad minim veniam, quis nostrud exerci tation ullamcorper suscipit lobortis nisl ut aliquip ex ea commodo consequat. Duis autem vel eum iriure dolor in hendrerit in vulputate velit esse molestie consequat, vel illum dolore eu feugiat nulla facilisis at vero eros et accumsan et iusto odio dignissim qui blandit praesent luptatum zzril delenit augue duis dolore te feugait nulla facilisi.</p>
    <p class="closing">Mit freundlichen Grüßen,</p>
    <span class="signature" role="img" aria-label="Unterschrift"></span>
    <div class="signer">Jonas Keller<br>Projektmanager</div>
  </div>

  <div class="mascot" role="img" aria-label="Platz für die Maskottchen-Illustration der Marke"></div>

  <div class="footer-stripe"><span></span><span></span><span></span></div>
  <footer class="footer">
    <div class="footer-col" style="left:101px">
      <span class="brand">Planorix GmbH</span><br>
      Ahornweg 23<br>
      54321 Beispielstadt
    </div>
    <div class="footer-col" style="left:226px">
      <b>Geschäftsführer:</b> Felix Brandt<br>
      Handelsregister Beispielstadt<br>
      Beispielstädter Bank<br>
      IBAN: DE40 7711 2093 5518 02<br>
      BIC: BSPKDE31XXX
    </div>
    <div class="footer-col" style="left:413px">
      <b>Bankverbindung</b><br>
      IBAN: DE40 7711 2093 5518 02<br>
      BIC: BSPKDE31XXX<br>
      USt-IdNr: DE31740586
    </div>
    <div class="footer-col" style="left:595px">
      <b>Kontakt</b><br>
      <b>Telefon:</b> 04567 - 21 90 35 0<br>
      <b>Telefax:</b> 04567 - 21 90 35 - 134<br>
      <b>E-Mail:</b> info@planorix.de<br>
      <b>Webseite:</b> www.planorix.de
    </div>
  </footer>
</main>
</body>
</html>
```